Bref créative
bussines & member card for Jewelry shop
Marten.K Gold & Jewelry
Bright & Fun-filled
Marten.K
Gold & Jewelry
Jln.Mayor Sulaiman Gg.Kedua No.7B
Pasar Tanjung-Rambutan
Medan-Sumatera Utara
Indonesia
marten.kgoldworks@lumarel.example
this is our logo

```html
<!DOCTYPE html>
<html lang="en">
<head>
<meta charset="utf-8">
<title>Marten.K Gold &amp; Jewelry – Business Card</title>
<link href="https://fonts.googleapis.com/css2?family=Cinzel:wght@400;600&display=swap" rel="stylesheet">
<style>
  :root {
    --backdrop: #2b2b2d;
    --card: #f4f4f4;
    --card-edge: #e2e2e2;
    --ink: #1c1c1c;
    --ink-soft: #3a3a3a;
    --rule: #1c1c1c;
  }
  * { margin: 0; padding: 0; box-sizing: border-box; }
  html, body {
    width: 1200px; height: 901px; overflow: hidden;
    background: var(--backdrop);
    font-family: "Cinzel", "Times New Roman", serif;
  }
  .canvas {
    width: 1200px; height: 901px;
    display: flex; align-items: center; justify-content: center;
  }
  .business-card {
    position: relative;
    width: 1000px; height: 571px;
    background: linear-gradient(135deg, #ffffff 0%, var(--card) 55%, var(--card-edge) 100%);
    border-radius: 26px;
    color: var(--ink);
  }
  .brand {
    position: absolute;
    left: 70px; top: 120px; width: 360px;
    display: flex; flex-direction: column; align-items: center;
  }
  .brand-mark {
    width: 210px; height: 210px;
    border: 3px solid var(--ink);
    border-radius: 50%;
  }
  .brand-name {
    margin-top: 34px;
    font-size: 22px; font-weight: 400;
    letter-spacing: 4px;
    text-align: center;
    color: var(--ink);
  }
  .divider {
    position: absolute;
    left: 470px; top: 140px;
    width: 2px; height: 320px;
    background: var(--rule);
  }
  .contact {
    position: absolute;
    left: 500px; top: 140px;
  }
  .contact-name {
    font-size: 26px; font-weight: 600;
    letter-spacing: 2px;
  }
  .address {
    margin-top: 58px;
    list-style: none;
    font-size: 17px; line-height: 25px;
    letter-spacing: 0.5px;
    color: var(--ink-soft);
  }
  .channels {
    margin-top: 28px;
    list-style: none;
    font-size: 17px; line-height: 25px;
    letter-spacing: 0.5px;
    color: var(--ink-soft);
  }
  .channels li { display: flex; align-items: center; gap: 10px; }
  .channels svg { width: 16px; height: 16px; flex: none; fill: var(--ink); }
</style>
</head>
<body>
<main class="canvas">
  <section class="business-card">
    <div class="brand">
      <div class="brand-mark"></div>
      <p class="brand-name">Marten.K Gold &amp; Jewelry</p>
    </div>

    <div class="divider"></div>

    <div class="contact">
      <h1 class="contact-name">Marten.K</h1>
      <ul class="address">
        <li>Jln.Mayor Sulaiman Gg.Kedua No.7B</li>
        <li>Pasar Tanjung-Rambutan</li>
        <li>Medan-Sumatera Utara</li>
        <li>Indonesia</li>
      </ul>
      <ul class="channels">
        <li>
          <svg viewBox="0 0 16 16" aria-hidden="true"><path d="M1 5c0-2 3-3 7-3s7 1 7 3v1h-4V5H5v1H1z"/><rect x="3" y="7" width="10" height="7" rx="1"/></svg>
          061-4725816
        </li>
        <li>
          <svg viewBox="0 0 16 16" aria-hidden="true"><rect x="4" y="1" width="8" height="14" rx="1.5"/><rect x="5.5" y="3" width="5" height="8" fill="#f4f4f4"/></svg>
          081274430615, 08127743902
        </li>
        <li>
          <svg viewBox="0 0 16 16" aria-hidden="true"><rect x="1" y="3" width="14" height="10" rx="1"/><path d="M1.5 4l6.5 5 6.5-5" stroke="#f4f4f4" stroke-width="1.4" fill="none"/></svg>
          marten.kgoldworks@lumarel.example
        </li>
      </ul>
    </div>
  </section>
</main>
</body>
</html>
```